General Surgeon flyer to be distributed to GPs

I am a general surgeon and I would like to have a flyer designed aiming to introduce myself to GPs.

Name: Dr Tobias Kellingford MD, FRACS
Address: Suite 9A, Brayfield private hospital, 418 Copperleaf Parade, Wantirna, VIC, 3152
T: (03) 9561 8027
F: (03) 9773 4105
E: referrals@yourtheatrewellnessportal.com.au
Website: www.yourtheatrewellnessportal.com.au

Tobias is a highly trained general surgeon, having completed extensive surgical training at Coastal Ridge health, Pellbrook and Tarrowby Health networks. He further specialized by completing a fellowship in Oesophagogastric and Bariatric Surgery at Greywater Infirmary Melbourne, one of Victoria’s leading Upper GI surgical centres.

With expertise in both advanced laparoscopic and open surgical techniques, he performs a wide range of procedures involving the gastrointestinal system, abdominal wall hernias, as well as other major and minor general surgical operations. In addition to holding appointments at Coastal Ridge Health, he also operates at Brayfield and Ashcombe Private Hospitals.

Dr Kellingford is committed to providing patient-centred care with a focus on surgical precision, safety, and long-term health outcomes.

He is also fluent in Farsi/Pesrian.
Outside of surgery, Tobias enjoys playings classical piano and spending time with his 6-year-old Bordoodle on long walks.

Upper GI & Bariatric Surgery:
Hiatus hernia repair, sleeve gastrectomy, gastric bypass
General Surgery conditions:
Gallbladder Surgery: Laparoscopic cholecystectomy
Hernia Repair: Laparoscopic and open surgery (inguinal,
umbilical, incisional)
Anorectal Procedures: Haemorrhoidectomy, haemorrhoid banding
Hand Surgery: Carpal tunnel release, Lymph Node Biopsy
Ingrown Toenail Surgery
Skin & Soft Tissue Surgery: Skin cancer removal, lipoma and
sebaceous cyst excision
Emergency Surgery: Laparotomy, Appendicectomy, bowel resection
Endoscopy: Diagnostic and therapeutic procedures

```html
<!DOCTYPE html>
<html lang="en">
<head>
<meta charset="utf-8">
<title>Dr Tobias Kellingford – GP Flyer</title>
<link href="https://fonts.googleapis.com/css2?family=Montserrat:ital,wght@0,400;0,500;0,600;0,700;0,800;1,400;1,500;1,700&display=swap" rel="stylesheet">
<style>
  :root{
    --stage:#e4e5e7;
    --slate:#a3a5a8;
    --slate-light:#b9bbbe;
    --band-blue:#5a84b8;
    --band-blue-deep:#4d75a8;
    --ice:#dce9f8;
    --navy:#0f3158;
    --navy-deep:#0b2748;
    --brand-blue:#1b4fa3;
    --white:#ffffff;
    --ink-navy:#0f2a4e;
  }
  *{box-sizing:border-box;margin:0;padding:0}
  html,body{width:1200px;height:800px;overflow:hidden}
  body{background:var(--stage);font-family:"Montserrat",Arial,sans-serif;position:relative}

  .flyer{
    position:absolute;left:330px;top:12px;width:540px;height:776px;
    background:var(--slate);overflow:hidden;
    box-shadow:0 6px 24px rgba(0,0,0,.18);
  }
  .region-map{
    position:absolute;left:30px;top:150px;width:480px;height:380px;
    background:radial-gradient(closest-side,var(--slate-light) 0%,var(--slate-light) 70%,rgba(185,187,190,0) 100%);
  }
  .doctor-name{
    position:absolute;left:38px;top:46px;color:var(--white);
    font-weight:800;font-size:32px;line-height:1.04;text-transform:uppercase;letter-spacing:.5px;
  }
  .doctor-name .credentials{display:block;font-weight:600;font-size:19px;margin-top:6px;letter-spacing:.3px}

  .brand{
    position:absolute;right:34px;top:96px;display:flex;flex-direction:column;align-items:flex-end;gap:10px;
    color:var(--brand-blue);font-weight:600;font-size:12px;letter-spacing:1.4px;text-transform:uppercase;line-height:1.4;text-align:right;
  }
  .brand-dot{width:40px;height:40px;border-radius:50%;background:var(--brand-blue);flex:none;margin-right:20px}

  .portrait{
    position:absolute;left:135px;top:170px;width:290px;height:330px;
    border-radius:145px 145px 0 0;
    background:linear-gradient(180deg,#b79b86 0%,#a58b7a 38%,#8fb3e0 58%,#3f4f7c 72%,#3a4a75 100%);
  }

  .contact-band{position:absolute;left:0;top:488px;width:100%;height:84px}
  .contact-band svg{position:absolute;inset:0}
  .phone{
    position:absolute;left:0;right:0;top:500px;display:flex;justify-content:center;align-items:center;gap:12px;
    color:var(--white);font-weight:700;font-size:36px;letter-spacing:.5px;
  }
  .web-strip{
    position:absolute;left:0;top:572px;width:100%;height:54px;background:var(--ice);
    color:var(--ink-navy);
  }
  .web-strip .website{position:absolute;left:0;right:0;top:4px;text-align:center;font-size:15px;letter-spacing:2px}
  .web-strip .email{position:absolute;left:26px;bottom:6px;font-size:11px;letter-spacing:1px}
  .web-strip .fax{position:absolute;right:26px;bottom:4px;font-size:14px;font-weight:700;font-style:italic;display:flex;align-items:center;gap:6px}

  .bio-panel{
    position:absolute;left:0;top:626px;width:100%;height:150px;
    background:linear-gradient(180deg,var(--navy) 0%,var(--navy-deep) 100%);
    color:var(--white);padding:16px 34px 0;
  }
  .bio-panel p{font-size:11.5px;line-height:1.55;text-align:justify;font-style:italic;letter-spacing:.3px}
  .see-back{
    display:flex;align-items:center;gap:8px;width:max-content;margin:14px auto 0;
    border:1.5px solid var(--white);border-radius:20px;padding:5px 22px;
    font-size:12px;font-style:italic;letter-spacing:.4px;
  }
</style>
</head>
<body>
  <article class="flyer">
    <div class="region-map" role="img" aria-label="Faint map of Australia behind the portrait"></div>

    <h1 class="doctor-name">Dr Tobias<br>Kellingford<span class="credentials">MD, FRACS</span></h1>

    <div class="brand">
      <span class="brand-dot"></span>
      <span>Meridian Surgeons<br>Collective</span>
    </div>

    <div class="portrait" role="img" aria-label="Portrait photo of Dr Tobias Kellingford in a navy suit and blue tie"></div>

    <div class="contact-band">
      <svg width="540" height="84" viewBox="0 0 540 84" preserveAspectRatio="none">
        <path d="M0 10 C120 0 200 22 300 14 S460 2 540 12 L540 84 L0 84 Z" fill="var(--band-blue)"/>
        <path d="M300 84 C360 60 430 70 540 52 L540 84 Z" fill="var(--band-blue-deep)"/>
      </svg>
    </div>
    <div class="phone">
      <svg width="20" height="32" viewBox="0 0 20 32" aria-hidden="true">
        <rect x="2" y="1.5" width="16" height="29" rx="3" fill="none" stroke="var(--white)" stroke-width="2"/>
        <line x1="7" y1="26" x2="13" y2="26" stroke="var(--white)" stroke-width="2"/>
      </svg>
      <span>(03) 9561 8027</span>
    </div>

    <div class="web-strip">
      <div class="website">www.yourtheatrewellnessportal.com.au</div>
      <div class="email">referrals@yourtheatrewellnessportal.com.au</div>
      <div class="fax">
        <svg width="16" height="14" viewBox="0 0 16 14" aria-hidden="true">
          <rect x="4" y="1" width="8" height="4" fill="none" stroke="var(--ink-navy)" stroke-width="1.4"/>
          <rect x="1" y="5" width="14" height="6" rx="1" fill="none" stroke="var(--ink-navy)" stroke-width="1.4"/>
          <rect x="4" y="9" width="8" height="4" fill="var(--ice)" stroke="var(--ink-navy)" stroke-width="1.4"/>
        </svg>
        <span>(03) 9773 4105</span>
      </div>
    </div>

    <section class="bio-panel">
      <p>Tobias is a highly trained general surgeon, having completed extensive surgical training at Coastal Ridge health, Pellbrook and Tarrowby Health networks. He further specialized by completing a fellowship in Oesophagogastric and Bariatric Surgery at Greywater Infirmary Melbourne, one of Victoria’s leading Upper GI surgical centres.</p>
      <div class="see-back">
        <svg width="16" height="12" viewBox="0 0 16 12" aria-hidden="true">
          <path d="M2 11 L5 1 L8 11 M8 11 L11 1 L14 11" fill="none" stroke="var(--white)" stroke-width="1.3"/>
        </svg>
        <span>See Back for More</span>
      </div>
    </section>
  </article>
</body>
</html>
```